Corporate Design für Büroservice
Zielgruppe
Wir bieten Dienstleistungen rund ums Büro wie z.b. Buchhaltung, Kommunikation ... für Unternehmen an.
Wir benötigen eine neue Website, da wir unser Unternehmen vergrößern und zusätzliche Dienstleitungen anbieten möchten.
Aufgabenstellung
Vorgaben haben wir keine nur sollte das Logo und der Rest zu unserer Branche passen und ansprechend wirken. Zudem sollte es Kompetenz und Seriosität vermitteln.
Visitenkarte und Briefbogen bitte mit den beigefügten Daten erstellen.

```html
<!DOCTYPE html>
<html lang="de">
<head>
<meta charset="utf-8">
<title>Brevalis Office – Corporate Design</title>
<link rel="stylesheet" href="https://fonts.googleapis.com/css2?family=Arimo:wght@400;700&display=swap">
<style>
  :root {
    --brand-blue: #2f8fd8;
    --ink-gray: #7a7a7a;
    --text-dark: #4a4a4a;
    --band-light: #f2f2f2;
    --band-white: #ffffff;
    --band-gray: #c7c7c7;
    --tile-dark: #9b9b9b;
    --card-gray: #c9c9c9;
    --paper: #ffffff;
    --flap: #cfcfcf;
  }
  * { box-sizing: border-box; margin: 0; padding: 0; }
  html, body { width: 1200px; height: 556px; overflow: hidden; }
  body {
    font-family: "Arimo", Arial, sans-serif;
    background: var(--band-light);
    position: relative;
    color: var(--text-dark);
  }
  .band { position: absolute; }
  .band--white { left: 0; top: 112px; width: 1200px; height: 170px; background: var(--band-white); }
  .band--gray { left: 0; top: 282px; width: 787px; height: 168px; background: var(--band-gray); }
  .tile { position: absolute; top: 450px; height: 85px; width: 207px; }
  .tile--dark { left: 0; background: var(--tile-dark); }
  .tile--white { left: 207px; background: var(--band-white); }

  .wordmark { position: absolute; display: flex; align-items: center; white-space: nowrap; }
  .wordmark__square { background: var(--brand-blue); flex: none; }
  .wordmark__name { font-weight: 400; letter-spacing: -0.01em; }

  .wordmark--hero { left: 44px; top: 175px; }
  .wordmark--hero .wordmark__square { width: 40px; height: 40px; margin-right: 30px; }
  .wordmark--hero .wordmark__name { font-size: 38px; color: var(--ink-gray); }

  .wordmark--inverse { left: 44px; top: 343px; }
  .wordmark--inverse .wordmark__square { width: 40px; height: 40px; margin-right: 30px; background: #fff; }
  .wordmark--inverse .wordmark__name { font-size: 38px; color: #fff; }

  .wordmark--small-dark { left: 34px; top: 483px; }
  .wordmark--small-dark .wordmark__square { width: 16px; height: 16px; margin-right: 12px; background: #fff; }
  .wordmark--small-dark .wordmark__name { font-size: 16px; color: #fff; }

  .wordmark--small-light { left: 246px; top: 483px; }
  .wordmark--small-light .wordmark__square { width: 16px; height: 16px; margin-right: 12px; background: #c4c4c4; }
  .wordmark--small-light .wordmark__name { font-size: 16px; color: #bdbdbd; }

  .sheet {
    position: absolute; background: var(--paper);
    box-shadow: 0 2px 8px rgba(0,0,0,0.18);
  }
  .letterhead { left: 418px; top: 33px; width: 341px; height: 480px; }
  .letterhead .wordmark { right: 34px; top: 40px; }
  .letterhead .wordmark__square { width: 13px; height: 13px; margin-right: 8px; }
  .letterhead .wordmark__name { font-size: 13px; color: var(--ink-gray); }
  .letterhead__sender {
    position: absolute; left: 38px; top: 94px;
    font-size: 4.8px; color: #555; border-bottom: 0.5px solid #999; padding-bottom: 1px;
  }
  .letterhead__body {
    position: absolute; left: 38px; top: 110px; width: 268px;
    font-size: 4.4px; line-height: 5.8px; color: #555; text-align: justify;
  }
  .letterhead__body p { margin-bottom: 6px; }
  .letterhead__body p.gap { margin-top: 12px; }
  .letterhead__signature {
    position: absolute; left: 222px; top: 290px; width: 80px; height: 30px;
    background: linear-gradient(90deg, #eef0f5, #dfe3ec);
  }
  .letterhead__rule { position: absolute; left: 0; right: 0; top: 448px; height: 1px; background: var(--brand-blue); }
  .letterhead__footer {
    position: absolute; left: 40px; right: 30px; top: 454px;
    display: flex; gap: 42px; font-size: 3.8px; line-height: 5px; color: #777;
  }

  .card { position: absolute; top: 35px; height: 110px; }
  .card--front { left: 791px; width: 179px; background: var(--card-gray); }
  .card--front .wordmark { left: 70px; top: 36px; }
  .card--front .wordmark__square { width: 38px; height: 38px; margin: 0; }
  .card--back { left: 996px; width: 169px; background: var(--paper); }
  .card--back .wordmark { left: 30px; top: 21px; }
  .card--back .wordmark__square { width: 12px; height: 12px; margin-right: 7px; }
  .card--back .wordmark__name { font-size: 12.5px; color: var(--ink-gray); }
  .card__person { position: absolute; left: 26px; top: 56px; font-size: 6.5px; color: #666; }
  .card__person strong { display: block; font-weight: 700; }
  .card__person span { font-size: 5px; }
  .card__contacts { position: absolute; left: 88px; top: 55px; font-size: 3.9px; line-height: 7px; color: #777; list-style: none; }
  .card__contacts li { display: flex; align-items: center; gap: 4px; }
  .card__contacts svg { width: 4px; height: 4px; fill: var(--brand-blue); flex: none; }

  .envelope { position: absolute; left: 786px; width: 382px; height: 167px; background: var(--paper); }
  .envelope--front { top: 163px; }
  .envelope__window {
    position: absolute; left: 24px; top: 81px; width: 152px; height: 56px;
    border-radius: 9px; background: #f7f7f7; box-shadow: inset 0 0 3px rgba(0,0,0,0.15);
  }
  .envelope--front .wordmark { right: 28px; top: 114px; }
  .envelope--front .wordmark__square { width: 10px; height: 10px; margin-right: 6px; }
  .envelope--front .wordmark__name { font-size: 11px; color: var(--ink-gray); }
  .envelope--back { top: 343px; }
  .envelope__flap { position: absolute; left: 0; top: 0; width: 382px; height: 45px; }
  .envelope--back .envelope__mark {
    position: absolute; left: 183px; top: 17px; width: 16px; height: 16px; background: var(--brand-blue);
  }
  .envelope--back .wordmark { left: 0; right: 0; top: 142px; justify-content: center; }
  .envelope--back .wordmark__name { font-size: 10.5px; color: #888; }
</style>
</head>
<body>
  <div class="band band--white"></div>
  <div class="band band--gray"></div>
  <div class="tile tile--dark"></div>
  <div class="tile tile--white"></div>

  <div class="wordmark wordmark--hero"><span class="wordmark__square"></span><span class="wordmark__name">Brevalis Office</span></div>
  <div class="wordmark wordmark--inverse"><span class="wordmark__square"></span><span class="wordmark__name">Brevalis Office</span></div>
  <div class="wordmark wordmark--small-dark"><span class="wordmark__square"></span><span class="wordmark__name">Brevalis Office</span></div>
  <div class="wordmark wordmark--small-light"><span class="wordmark__square"></span><span class="wordmark__name">Brevalis Office</span></div>

  <section class="sheet letterhead" aria-label="Briefbogen">
    <div class="wordmark"><span class="wordmark__square"></span><span class="wordmark__name">Brevalis Office</span></div>
    <p class="letterhead__sender">Your Company · Your adress 12 · 34567 Your town</p>
    <div class="letterhead__body">
      <p>Lorem ipsum dolor sit amet, consectetur adipiscing elit. Maecenas porttitor augue justo, sit amet egestas sapien luctus ultrices. Donec arcu dolor, tincidunt sit amet mi id, laoreet pretium enim. Sed fermentum, dui vel hendrerit sodales, lectus nibh molestie tortor, id fermentum velit urna a diam. Aenean efficitur turpis ex lorem porttitor et tincidunt leo aliquam. Fusce vel facilisis massa, euismod ullamcorper neque. Suspendisse sodales at nisl ut eleifend. Aliquam nec varius diam. Donec quis enim dictum, tempus nunc et, auctor quam. Suspendisse potenti. Quisque accumsan egestas metus. Morbi faucibus, libero id rhoncus feugiat, dui tellus aliquet purus, a porta leo sem et nunc. Maecenas pretium sit amet mi id vulputate. Quisque pharetra nisi ac gravida dapibus. Aenean sit amet augue diam. Vivamus dictum dolor ut eros egestas blandit. Aenean sagittis consequat tortor, ac dictum nunc varius vel.</p>
      <p>Phasellus id ante id ipsum cursus luctus. Praesent purus elit, ornare sit amet ultricies ac, dignissim a eros. Phasellus vestibulum odio et ipsum mattis maximus. Vivamus suscipit pulvinar tellus eu congue. Aenean quis dui varius, ullamcorper arcu sit amet, vehicula odio. Nunc dui tellus, blandit lacinia sapien eget, venenatis porttitor ex. Vivamus tortor dolor, convallis non nisi sit amet, rhoncus lobortis nisi. Sed molestie viverra elit, sit amet condimentum mi finibus et. Fusce molestie lorem id nulla rhoncus, quis dapibus ipsum pharetra. Cras est enim, congue at purus vitae, tempor lacinia dolor.</p>
      <p class="gap">Lorem ipsum dolor sit amet, consectetur adipiscing elit. Maecenas porttitor augue justo, sit amet egestas sapien luctus ultrices. Donec arcu dolor, tincidunt sit amet mi id, laoreet pretium enim. Sed fermentum, dui vel hendrerit sodales, lectus nibh molestie tortor, id fermentum velit urna a diam. Aenean efficitur turpis ex lorem porttitor et tincidunt leo aliquam. Fusce vel facilisis massa, euismod ullamcorper neque. Suspendisse sodales at nisl ut eleifend. Aliquam nec varius diam. Donec quis enim dictum, tempus nunc et, auctor quam. Suspendisse potenti. Quisque accumsan egestas metus. Morbi faucibus, libero id rhoncus feugiat, dui tellus aliquet purus, a porta leo sem et nunc. Maecenas pretium sit amet mi id vulputate. Aenean sit amet augue diam. Vivamus dictum dolor ut eros egestas blandit. Aenean sagittis consequat tortor, ac dictum nunc varius vel.</p>
      <p>Phasellus id ante id ipsum cursus luctus. Praesent purus elit, ornare sit amet ultricies ac, dignissim a eros. Phasellus vestibulum odio et ipsum mattis maximus. Vivamus suscipit pulvinar tellus eu congue. Aenean quis dui varius, ullamcorper arcu sit amet, vehicula odio. Nunc dui tellus, blandit lacinia sapien eget, venenatis porttitor ex. Vivamus tortor dolor, convallis non nisi sit amet, rhoncus lobortis nisi. Sed molestie viverra elit, sit amet condimentum mi finibus et. Fusce molestie lorem id nulla rhoncus, quis dapibus ipsum pharetra. Cras est enim, congue at purus vitae, tempor lacinia dolor.</p>
    </div>
    <div class="letterhead__signature" role="img" aria-label="Handschriftliche Unterschrift"></div>
    <div class="letterhead__rule"></div>
    <div class="letterhead__footer">
      <div>Your Company<br>CEO Your Name<br>Your adress 12<br>34567 Your Town</div>
      <div>1234 - 56 78 90 00<br>1234 - 56 78 90 01<br>your.name@your-web.de<br>www.your-web.de</div>
      <div>Bankverbindung<br>Iban DE00 0000 0000 0000 00<br>BIC<br>UST-ID 000000000000</div>
    </div>
  </section>

  <section class="sheet card card--front" aria-label="Visitenkarte Vorderseite">
    <div class="wordmark"><span class="wordmark__square"></span></div>
  </section>

  <section class="sheet card card--back" aria-label="Visitenkarte Rückseite">
    <div class="wordmark"><span class="wordmark__square"></span><span class="wordmark__name">Brevalis Office</span></div>
    <p class="card__person"><strong>Your Name</strong><span>CEO</span></p>
    <ul class="card__contacts">
      <li><svg viewBox="0 0 10 10"><path d="M5 0a3.5 3.5 0 0 0-3.5 3.5C1.5 6 5 10 5 10s3.5-4 3.5-6.5A3.5 3.5 0 0 0 5 0z"/></svg>Your Adress 12, 34567 Your Town</li>
      <li><svg viewBox="0 0 10 10"><path d="M2 0h2l1 3-1.5 1a6 6 0 0 0 2.5 2.5L7 5l3 1v2c0 1-1 2-2 2A8 8 0 0 1 0 2c0-1 1-2 2-2z"/></svg>+00 123 456 789</li>
      <li><svg viewBox="0 0 10 10"><rect x="2.5" y="0" width="5" height="10" rx="1"/></svg>+00 123 456 789</li>
      <li><svg viewBox="0 0 10 10"><rect x="0" y="2" width="10" height="6"/></svg>your.name@your-web.de</li>
      <li><svg viewBox="0 0 10 10"><circle cx="5" cy="5" r="5"/></svg>www.your-web.de</li>
    </ul>
  </section>

  <section class="sheet envelope envelope--front" aria-label="Briefumschlag Vorderseite">
    <div class="envelope__window"></div>
    <div class="wordmark"><span class="wordmark__square"></span><span class="wordmark__name">Brevalis Office</span></div>
  </section>

  <section class="sheet envelope envelope--back" aria-label="Briefumschlag Rückseite">
    <svg class="envelope__flap" viewBox="0 0 382 45" aria-hidden="true">
      <polygon points="0,0 382,0 366,45 16,45" fill="var(--flap)"/>
    </svg>
    <span class="envelope__mark"></span>
    <div class="wordmark"><span class="wordmark__name">Brevalis Office</span></div>
  </section>
</body>
</html>
```